Business Card Design

Marla Quibbet
Artist of Contemporary/Modern/Representational Art
Contact: 0457219308
Please include my web site (thanks)! http://www.artvault913.com.au/marla-quibbet
And
Email: marlaquibbet@fernpost.example

Target Market(s)

Modern professional People who know what they like in modern contemporary art and have the means to purchase it.

Industry/Entity Type

Business

Contact Information for Business Card

Marla Quibbet
Contact: 0457219308

Font styles to use
Sans Serif

Requirements
Must have
• Simplicity & to the point
Keep the font modern/ contemporary
Nice to have
• A portrait of me and one piece of work on the business card (one on each side).
Should not have
• I'm not into butterflies.
No feminine style swirls
Nor I like swirls that look like tatoos

```html
<!DOCTYPE html>
<html lang="en">
<head>
<meta charset="utf-8">
<title>Marla Quibbet — Business Card</title>
<link rel="stylesheet" href="https://fonts.googleapis.com/css2?family=Exo+2:wght@300;400&display=swap">
<style>
  :root {
    --page: #ffffff;
    --card-black: #0d0d0d;
    --texture-dark: #1c1c1c;
    --texture-mid: #2a2a2a;
    --ink-white: #f4f4f4;
    --ink-soft: #d8d8d8;
    --rule-grey: #8a8a8a;
    --icon-grey: #7a7a7a;
    --portrait-warm: #d2501e;
    --portrait-deep: #8a3a2c;
    --city-green: #4f9a4a;
    --city-river: #2f86a6;
    --city-sky: #6fb9d2;
    --city-stone: #b89a7a;
    --facade-red: #d23a2a;
    --facade-yellow: #e0c23a;
    --facade-green: #79a050;
    --tape: #e8dcb0;
  }
  * { box-sizing: border-box; margin: 0; padding: 0; }
  html, body { width: 1200px; height: 1200px; overflow: hidden; background: var(--page); }
  body { position: relative; font-family: "Exo 2", sans-serif; }

  .card {
    position: absolute;
    left: 250px;
    width: 700px;
    height: 400px;
    overflow: hidden;
    box-shadow: 0 2px 10px rgba(0,0,0,0.18);
  }
  .card--front { top: 170px; background: var(--card-black); }
  .card--back { top: 630px; background: var(--city-green); }

  /* front */
  .front-texture {
    position: absolute; inset: 0;
    background:
      linear-gradient(90deg, var(--texture-mid) 0%, var(--card-black) 35%, var(--texture-dark) 60%, var(--card-black) 100%),
      var(--card-black);
    opacity: 0.9;
  }
  .name-rule {
    position: absolute; left: 0; top: 247px;
    width: 372px; height: 1px; background: var(--rule-grey);
  }
  .name {
    position: absolute; right: 338px; top: 206px;
    font-weight: 300; font-size: 28px; line-height: 34px; letter-spacing: 0.2em;
    color: var(--ink-white); white-space: nowrap;
  }
  .role {
    position: absolute; left: 90px; top: 256px; width: 270px;
    font-weight: 400; font-size: 13px; line-height: 1.35;
    color: var(--ink-soft); text-align: center; letter-spacing: 0.03em;
  }
  .contacts {
    position: absolute; left: 382px; top: 194px;
    list-style: none; display: flex; flex-direction: column; gap: 6px;
  }
  .contacts li {
    display: flex; align-items: center; gap: 6px;
    font-size: 12px; color: var(--ink-white); letter-spacing: 0.01em; white-space: nowrap;
  }
  .contact-icon {
    flex: none;
    width: 18px; height: 18px; background: var(--icon-grey);
    display: flex; align-items: center; justify-content: center; border-radius: 2px;
  }

  /* back */
  .back-city {
    position: absolute; inset: 0;
    background:
      radial-gradient(ellipse at 95% 0%, var(--city-sky) 0%, transparent 40%),
      linear-gradient(160deg, var(--city-stone) 0%, var(--city-green) 35%, var(--city-river) 55%, var(--city-green) 75%, #3e7a3a 100%);
  }
  .back-portrait {
    position: absolute; left: 0; top: 0; width: 260px; height: 400px;
    background: radial-gradient(ellipse at 30% 30%, var(--portrait-deep) 0%, var(--portrait-warm) 55%, rgba(210,80,30,0) 100%);
  }
  .snapshot {
    position: absolute; left: 395px; top: 185px; width: 270px; height: 185px;
    background: #fff; padding: 7px;
  }
  .snapshot-art {
    width: 100%; height: 100%;
    background: linear-gradient(90deg, var(--facade-red) 0%, var(--facade-red) 20%, var(--facade-green) 20%, var(--facade-green) 40%, var(--facade-red) 40%, var(--facade-red) 55%, var(--facade-yellow) 55%, var(--facade-yellow) 75%, var(--facade-green) 75%);
  }
  .tape {
    position: absolute; left: 640px; top: 165px; width: 30px; height: 70px;
    background: var(--tape); opacity: 0.85;
  }
</style>
</head>
<body>

<section class="card card--front" aria-label="Business card front">
  <div class="front-texture" role="img" aria-label="Dark monochrome artwork of a tree-lined avenue"></div>
  <div class="name-rule"></div>
  <h1 class="name">Marla Quibbet</h1>
  <p class="role">Artist of Contemporary/Modern/<br>Representational Art</p>
  <ul class="contacts">
    <li>
      <span class="contact-icon">
        <svg width="12" height="12" viewBox="0 0 24 24"><path fill="#fff" d="M6.6 10.8a15 15 0 0 0 6.6 6.6l2.2-2.2a1 1 0 0 1 1-.25 11.4 11.4 0 0 0 3.6.57 1 1 0 0 1 1 1V20a1 1 0 0 1-1 1A17 17 0 0 1 3 4a1 1 0 0 1 1-1h3.5a1 1 0 0 1 1 1c0 1.25.2 2.45.57 3.57a1 1 0 0 1-.25 1z"/></svg>
      </span>0457219308
    </li>
    <li>
      <span class="contact-icon">
        <svg width="12" height="12" viewBox="0 0 24 24" fill="none" stroke="#fff" stroke-width="2"><circle cx="12" cy="12" r="9"/><path d="M3 12h18M12 3c3 3 3 15 0 18M12 3c-3 3-3 15 0 18"/></svg>
      </span>http://www.artvault913.com.au/marla-quibbet
    </li>
    <li>
      <span class="contact-icon">
        <svg width="12" height="12" viewBox="0 0 24 24" fill="none" stroke="#fff" stroke-width="2"><rect x="3" y="5" width="18" height="14"/><path d="M3 6l9 7 9-7"/></svg>
      </span>marlaquibbet@fernpost.example
    </li>
  </ul>
</section>

<section class="card card--back" aria-label="Business card back">
  <div class="back-city" role="img" aria-label="Colourful painting of a city with river, stadium and parklands"></div>
  <div class="back-portrait" role="img" aria-label="Portrait photograph of the artist"></div>
  <div class="snapshot">
    <div class="snapshot-art" role="img" aria-label="Painting of a row of colourful townhouse facades"></div>
  </div>
  <div class="tape"></div>
</section>

</body>
</html>
```